A Maple Syrup Label for a Local Buniness

We are looking for a label for our maple syrup business. Our business currently sells honey, and we are expanding into maple syrup. Our Business name is "Brackley Honey" and we currently have a logo attached below. We would like to incorporate the bee and BH part, but the label could also read "Brackley Farms" with the words maple syrup. We do not want consumers to confuse the maple syrup jars with the honey jars. It should be clear that the jars contain maple syrup. We are open to new designs as well.

```html
<!DOCTYPE html>
<html lang="en">
<head>
<meta charset="utf-8">
<title>Brackley Farms Maple Syrup Label</title>
<link rel="stylesheet" href="https://fonts.googleapis.com/css2?family=Playfair+Display:wght@400;500&family=Montserrat:wght@700;800&display=swap">
<style>
  :root {
    --page: #f7f5f2;
    --paper: #ffffff;
    --stripe: #f3e4e4;
    --red: #c7353a;
    --red-light: #d85a5e;
    --ink: #232323;
    --white: #ffffff;
    --mark-tone: #ecdcdc;
  }
  html, body {
    margin: 0;
    padding: 0;
    width: 1200px;
    height: 960px;
    overflow: hidden;
    background: var(--page);
  }
  .label {
    display: block;
    width: 1200px;
    height: 960px;
  }
  .panel-paper { fill: var(--paper); }
  .panel-stripe { fill: var(--stripe); opacity: 0.55; }
  .panel-red { fill: url(#redFade); }
  .trim-red { fill: none; stroke: var(--red); stroke-width: 2.5; }
  .trim-ink { fill: none; stroke: var(--ink); stroke-width: 2.5; }
  .badge-shape { fill: url(#badgeFade); }
  .serif {
    font-family: "Playfair Display", "Bodoni Moda", serif;
    font-variant-numeric: lining-nums;
  }
  .badge-text {
    font-family: "Montserrat", sans-serif;
    font-weight: 800;
    fill: var(--white);
    text-anchor: middle;
  }
  .brand-mark-area { fill: url(#markFade); }
  .brand-name { font-size: 64px; font-weight: 400; fill: var(--ink); text-anchor: middle; letter-spacing: 1px; }
  .brand-sub { font-size: 62px; font-weight: 400; fill: var(--red); text-anchor: middle; letter-spacing: 5px; }
  .product-top { font-size: 130px; font-weight: 400; fill: var(--ink); text-anchor: middle; letter-spacing: 10px; }
  .product-bottom { font-size: 128px; font-weight: 400; fill: var(--white); text-anchor: middle; letter-spacing: 14px; }
  .net-weight { font-size: 34px; fill: var(--white); text-anchor: middle; }
</style>
</head>
<body>
<svg class="label" viewBox="0 0 1200 960" xmlns="http://www.w3.org/2000/svg">
  <defs>
    <linearGradient id="redFade" x1="0" x2="1" y1="0" y2="0">
      <stop offset="0" stop-color="#e48a8c"/>
      <stop offset="0.2" stop-color="#c7353a"/>
      <stop offset="0.8" stop-color="#c7353a"/>
      <stop offset="1" stop-color="#e48a8c"/>
    </linearGradient>
    <linearGradient id="badgeFade" x1="0" x2="1" y1="0" y2="0">
      <stop offset="0" stop-color="#d9585c"/>
      <stop offset="1" stop-color="#c7353a"/>
    </linearGradient>
    <radialGradient id="markFade" cx="0.5" cy="0.5" r="0.5">
      <stop offset="0" stop-color="#e2c9c9"/>
      <stop offset="1" stop-color="#f3e8e8"/>
    </radialGradient>
    <clipPath id="paperClip">
      <polygon points="231,253 337,253 600,68 863,253 969,253 969,577 231,577"/>
    </clipPath>
  </defs>

  <!-- upper white panel -->
  <polygon class="panel-paper" points="231,253 337,253 600,68 863,253 969,253 969,577 231,577"/>
  <g class="panel-stripes" clip-path="url(#paperClip)">
    <rect class="panel-stripe" x="231" y="110" width="738" height="14"/>
    <rect class="panel-stripe" x="231" y="150" width="738" height="14"/>
    <rect class="panel-stripe" x="231" y="190" width="738" height="14"/>
    <rect class="panel-stripe" x="231" y="230" width="738" height="14"/>
    <rect class="panel-stripe" x="231" y="270" width="738" height="14"/>
    <rect class="panel-stripe" x="231" y="310" width="738" height="14"/>
    <rect class="panel-stripe" x="231" y="350" width="738" height="14"/>
    <rect class="panel-stripe" x="231" y="390" width="738" height="14"/>
    <rect class="panel-stripe" x="231" y="430" width="738" height="14"/>
    <rect class="panel-stripe" x="231" y="470" width="738" height="14"/>
    <rect class="panel-stripe" x="231" y="510" width="738" height="14"/>
  </g>
  <polyline class="trim-red" points="231,266 341,266 600,84 859,266 969,266"/>

  <!-- lower red panel -->
  <polygon class="panel-red" points="231,577 969,577 969,707 863,707 600,892 337,707 231,707"/>
  <polyline class="trim-ink" points="231,697 341,697 600,878 859,697 969,697"/>

  <!-- natural badge -->
  <polygon class="badge-shape" points="231,248 382,208 382,374 301,423 231,374"/>
  <text class="badge-text" x="305" y="295" font-size="19">PURE AND</text>
  <text class="badge-text" x="305" y="340" font-size="48">100%</text>
  <text class="badge-text" x="305" y="369" font-size="19">NATURAL</text>

  <!-- brand -->
  <circle class="brand-mark-area" cx="600" cy="243" r="80" role="img" aria-label="Brackley Farms logo"/>
  <text class="serif brand-name" x="600" y="386">BRACKLEY</text>
  <text class="serif brand-sub" x="600" y="446">FARMS</text>

  <!-- product -->
  <text class="serif product-top" x="600" y="572">MAPLE</text>
  <text class="serif product-bottom" x="600" y="680">SYRUP</text>
  <text class="serif net-weight" x="600" y="788">340G</text>
</svg>
</body>
</html>
```